New Design for Willow Glow & Laser

The name of our company is Willow Glow & Laser, and this is our current website: www.WillowGlowLaser.example. We are looking for a fresh design mock-up of our website.
What is important to us?
> We want to maintain the same navigation.
> We want to use the same content (e.g., text, pictures, etc.)
> We want to maintain the color scheme.
> The website aims to get visitors to BOOK ONLINE or BUY ONLINE.
Essential instructions for designers:
> Please visit our current website and our social media accounts to get a better idea of our brand design.
> We want a mockup design for our home page, service page, pricing page, before & after page, shop deals page, careers page, contact pages, and blog pages.
> Color codes: #faa641, #222222, #fffffe, #ea8103
Target Market(s)
women 25 - 45
Number of Pages Required
5+ page
Look and feel

```html
<!DOCTYPE html>
<html lang="en">
<head>
<meta charset="utf-8">
<title>Careers – Willow Glow &amp; Laser</title>
<link href="https://fonts.googleapis.com/css2?family=Jost:wght@400;500;600;700&family=Roboto:wght@400;500&display=swap" rel="stylesheet">
<style>
:root{
  --orange:#faa641;
  --orange-deep:#ea8103;
  --ink:#222222;
  --paper:#fffffe;
  --line:#f6d9b3;
  --muted:#555555;
}
*{box-sizing:border-box;margin:0;padding:0}
html,body{width:1200px;height:4360px;overflow:hidden}
body{position:relative;background:var(--paper);color:var(--ink);font-family:"Roboto",sans-serif}
.abs{position:absolute}

/* header */
.site-header{position:absolute;left:0;top:0;width:1200px;height:71px;background:var(--paper)}
.brand{position:absolute;display:flex;align-items:center;gap:8px;font-family:"Jost",sans-serif;font-weight:700;color:var(--ink);white-space:nowrap}
.brand-dot{border-radius:50%;background:var(--orange);flex:none}
.nav{position:absolute;top:27px;font-family:"Jost",sans-serif;font-size:13px;font-weight:500;color:var(--ink)}
.nav.active{color:var(--orange)}
.pill{position:absolute;border-radius:20px;font-family:"Jost",sans-serif;font-size:12.5px;font-weight:500;display:flex;align-items:center;justify-content:center}
.pill.outline{border:1.5px solid var(--orange);color:var(--orange);background:var(--paper)}
.pill.solid{background:var(--orange);color:var(--paper)}

/* hero */
.hero{position:absolute;left:0;top:71px;width:1200px;height:288px;background:linear-gradient(90deg,#3a3330 0%,#6d5a50 35%,#a58a78 60%,#7a6a60 100%)}
.hero-title{left:140px;top:174px;font-family:"Jost",sans-serif;font-size:44px;font-weight:500;color:var(--paper)}
.crumbs{left:140px;top:229px;font-size:12.5px;color:var(--paper)}
.crumbs span{color:var(--orange)}

.section-title{position:absolute;left:0;width:1200px;text-align:center;font-family:"Jost",sans-serif;font-weight:600;color:var(--ink)}

/* intro */
.portrait{left:140px;top:511px;width:332px;height:332px;border-radius:50%;background:radial-gradient(circle at 50% 40%,#c9a995 0%,#8c6f60 55%,#2b2523 100%)}
.portrait-ring{left:150px;top:500px;width:330px;height:352px;border:1.5px solid var(--orange);border-radius:50%;transform:rotate(-12deg)}
.job-heading{left:599px;top:576px;font-family:"Jost",sans-serif;font-size:32px;font-weight:600;line-height:40px;color:var(--ink)}
.job-text{left:600px;top:673px;width:440px;font-size:13px;line-height:22px;color:var(--ink)}

/* accordion */
.acc{position:absolute;left:140px;width:918px;border:1.5px solid var(--orange);border-radius:12px;background:var(--paper)}
.acc-title{position:absolute;left:21px;font-family:"Jost",sans-serif;font-size:17px;font-weight:500;color:var(--ink)}
.acc-plus{position:absolute;right:18px;font-family:"Jost",sans-serif;font-size:26px;color:var(--orange);font-weight:500}
.acc-open-head{position:absolute;left:-1.5px;top:-1.5px;width:918px;height:57px;background:var(--orange);border-radius:12px 12px 0 0}
.acc-open-head .acc-title,.acc-open-head .acc-plus{color:var(--paper)}
.acc-body{position:absolute;left:21px;top:64px;width:880px;font-size:12px;line-height:23px;color:var(--ink)}

/* gallery */
.photo{position:absolute;border-radius:12px}

/* form */
.form-card{left:140px;top:2052px;width:918px;height:359px;border:1.5px solid var(--orange);border-radius:18px}
.field{position:absolute;border:1px solid #f1ede8;border-radius:10px;background:var(--paper);box-shadow:0 1px 4px rgba(0,0,0,.04)}
.field span{position:absolute;left:21px;top:18px;font-family:"Jost",sans-serif;font-size:12.5px;font-weight:500;color:#444}
.q-label{position:absolute;left:140px;font-family:"Jost",sans-serif;font-size:14px;font-weight:500;color:var(--ink)}
.radio{position:absolute;display:flex;align-items:center;gap:14px;font-size:12px;color:var(--ink)}
.radio i{display:block;width:21px;height:21px;border:1px solid #e6b98a;border-radius:50%}
.hint{position:absolute;left:140px;font-size:12px;color:var(--orange)}
.hint b{font-weight:400;color:var(--ink)}
.apply-btn{left:477px;top:3323px;width:248px;height:39px;border-radius:20px;background:var(--orange);color:var(--paper);font-family:"Jost",sans-serif;font-size:16px;font-weight:500;display:flex;align-items:center;justify-content:center}

/* contact cta */
.cta-photo{left:545px;top:3437px;width:655px;height:430px;border-radius:200px 0 0 0;background:linear-gradient(120deg,#e9e3dc 0%,#5a4a44 45%,#1f1c1c 75%,#c9b8a8 100%)}
.cta-circle{left:198px;top:3643px;width:264px;height:264px;border-radius:50%;background:var(--orange);text-align:center}
.cta-circle p{position:absolute;left:0;top:64px;width:264px;font-family:"Jost",sans-serif;font-size:21px;font-weight:600;line-height:30px;color:var(--paper)}
.cta-btn{position:absolute;left:76px;top:172px;width:112px;height:34px;border-radius:18px;background:var(--ink);color:var(--paper);font-size:11.5px;font-family:"Jost",sans-serif;display:flex;align-items:center;justify-content:center}

/* footer */
.footer{position:absolute;left:0;top:3880px;width:1200px;height:480px;background:#000}
.foot-h{position:absolute;font-family:"Jost",sans-serif;font-size:16px;font-weight:600;color:var(--paper)}
.foot-h::before{content:"";position:absolute;left:0;top:-12px;width:30px;height:2px;background:var(--orange)}
.foot-t{position:absolute;font-size:12px;line-height:19px;color:var(--paper)}
.quick{position:absolute;left:505px;top:4076px;list-style:none}
.quick li{height:24px;display:flex;align-items:center;gap:10px;font-size:12px;color:var(--paper);letter-spacing:.3px}
.quick li::before{content:"";width:6px;height:6px;border-radius:50%;background:var(--orange)}
.quick li.on{color:var(--orange)}
.news-input{left:777px;top:4132px;width:283px;height:34px;border-radius:18px;background:var(--paper);font-size:12px;color:#777;padding:10px 16px}
.news-btn{left:777px;top:4178px;width:141px;height:34px;border-radius:18px;background:var(--orange);color:var(--paper);font-family:"Jost",sans-serif;font-size:17px;font-weight:500;display:flex;align-items:center;justify-content:center}
.social{position:absolute;top:4300px;width:30px;height:30px;border-radius:50%;border:1px solid var(--paper)}
</style>
</head>
<body>

<header class="site-header">
  <div class="brand" style="left:149px;top:22px;font-size:16px;letter-spacing:.5px">
    <span class="brand-dot" style="width:24px;height:24px"></span>WILLOW GLOW &amp; LASER
  </div>
  <span class="nav" style="left:406px">Home</span>
  <span class="nav" style="left:469px">Services ⌄</span>
  <span class="nav" style="left:556px">Pricing ⌄</span>
  <span class="nav active" style="left:636px">About ⌄</span>
  <span class="nav" style="left:711px">Blog</span>
  <span class="nav" style="left:765px">Contact</span>
  <div class="pill outline" style="left:840px;top:20px;width:105px;height:31px">Book Online</div>
  <div class="pill solid" style="left:960px;top:20px;width:98px;height:31px">Buy Online</div>
</header>

<section class="hero" role="img" aria-label="Photo of two smiling clinic team members"></section>
<h1 class="abs hero-title">Careers</h1>
<p class="abs crumbs">Home &nbsp;»&nbsp; About &nbsp;»&nbsp; <span>Careers</span></p>

<h2 class="section-title" style="top:434px;font-size:30px">CAREERS</h2>

<div class="abs portrait-ring"></div>
<div class="abs portrait" role="img" aria-label="Photo of a team member holding a business card"></div>

<h2 class="abs job-heading">JOB OPPORTUNITIES AT<br>WILLOW GLOW &amp; LASER</h2>
<p class="abs job-text">To apply to one or more open positions, then please complete an application below. Please note that the application will ask for your recent resume.</p>
<div class="pill outline" style="left:601px;top:743px;width:149px;height:31px;font-size:12px">Available Positions</div>
<div class="pill solid" style="left:762px;top:743px;width:122px;height:31px;font-size:12px">Apply Today!</div>

<!-- positions -->
<div class="acc" style="top:980px;height:58px"><span class="acc-title" style="top:16px">Clinic Manager/Sales Manager</span><span class="acc-plus" style="top:10px">+</span></div>
<div class="acc" style="top:1053px;height:115px">
  <div class="acc-open-head"><span class="acc-title" style="top:16px">Certified Laser Technician</span><span class="acc-plus" style="top:10px">-</span></div>
  <p class="acc-body">A laser hair removal technician's role starts by helping patients understand the science, the benefits, and the risks associated with this cosmetic treatment. Using this information, laser hair removal technicians input laser settings to provide a safe, comfortable, and effective treatment.</p>
</div>
<div class="acc" style="top:1185px;height:58px"><span class="acc-title" style="top:16px">Registered Nurse</span><span class="acc-plus" style="top:10px">+</span></div>
<div class="acc" style="top:1256px;height:58px"><span class="acc-title" style="top:16px">Patient Coordinator</span><span class="acc-plus" style="top:10px">+</span></div>
<div class="acc" style="top:1329px;height:58px"><span class="acc-title" style="top:16px">Medical Director</span><span class="acc-plus" style="top:10px">+</span></div>

<!-- gallery -->
<div class="photo" style="left:140px;top:1513px;width:271px;height:346px;background:linear-gradient(160deg,#d8cbbd,#8a7464)" role="img" aria-label="Photo of a technician performing a laser treatment"></div>
<div class="photo" style="left:427px;top:1513px;width:166px;height:166px;background:linear-gradient(160deg,#6b5a4e,#1e1b1b)" role="img" aria-label="Portrait photo of a team member"></div>
<div class="photo" style="left:427px;top:1695px;width:166px;height:164px;background:linear-gradient(160deg,#c8b8a6,#3a3231)" role="img" aria-label="Photo of a team member in the clinic"></div>
<div class="photo" style="left:606px;top:1513px;width:273px;height:346px;background:linear-gradient(160deg,#d9c8b6,#5a4a44 60%,#241f1f)" role="img" aria-label="Photo of a client with a hand mirror and a team member"></div>
<div class="photo" style="left:892px;top:1513px;width:166px;height:166px;background:linear-gradient(160deg,#9ab0bf,#e8e1d8)" role="img" aria-label="Photo of a facial treatment"></div>
<div class="photo" style="left:892px;top:1695px;width:166px;height:164px;background:linear-gradient(160deg,#e6dfc6,#2e2a28)" role="img" aria-label="Photo of a cheerful team member"></div>

<h2 class="section-title" style="top:1978px;font-size:33px;font-weight:500">APPLICATION FOR EMPLOYMENT</h2>

<div class="abs form-card"></div>
<div class="field" style="left:183px;top:2094px;width:401px;height:56px"><span>First Name*</span></div>
<div class="field" style="left:613px;top:2094px;width:403px;height:56px"><span>Last Name*</span></div>
<div class="field" style="left:183px;top:2167px;width:401px;height:56px"><span>Preferred Name*</span></div>
<div class="field" style="left:613px;top:2167px;width:403px;height:56px"><span>Cell Phone</span></div>
<div class="field" style="left:183px;top:2240px;width:401px;height:56px"><span>Home Phone</span></div>
<div class="field" style="left:613px;top:2240px;width:403px;height:56px"><span>Work Phone</span></div>
<div class="field" style="left:183px;top:2313px;width:833px;height:56px"><span>Email*</span></div>

<p class="q-label" style="top:2451px">Full Time or Part Time*</p>
<label class="radio" style="left:140px;top:2486px"><i></i>Full Time</label>
<label class="radio" style="left:254px;top:2486px"><i></i>Part Time</label>

<p class="q-label" style="top:2534px">Which position are you interested in?*</p>
<label class="radio" style="left:140px;top:2569px"><i></i>Clinic Manager</label>
<label class="radio" style="left:358px;top:2569px"><i></i>Medical Director</label>
<label class="radio" style="left:565px;top:2569px"><i></i>Patient Coordinator</label>
<label class="radio" style="left:732px;top:2569px"><i></i>Aesthetician</label>
<label class="radio" style="left:140px;top:2605px"><i></i>Certified Laser Technician</label>
<label class="radio" style="left:358px;top:2605px"><i></i>Assistant Clinic Manager</label>
<label class="radio" style="left:565px;top:2605px"><i></i>Registered Nurse</label>

<div class="field" style="left:140px;top:2656px;width:918px;height:122px"><span>Introduction Message*</span></div>
<p class="hint" style="top:2792px">We kindly ask you to summarize your professional experience and what skills are relevant to the positions you're applying for.</p>

<p class="q-label" style="top:2844px">Preferred Location*</p>
<label class="radio" style="left:140px;top:2879px"><i></i>Tucson, AZ</label>
<label class="radio" style="left:341px;top:2879px"><i></i>Yuma, AZ</label>
<label class="radio" style="left:532px;top:2879px"><i></i>Tempe, AZ</label>
<label class="radio" style="left:732px;top:2879px"><i></i>Downtown Phoenix, AZ</label>

<div class="field" style="left:140px;top:2931px;width:918px;height:54px"><span>What is your desired pay?*</span></div>
<div class="field" style="left:140px;top:3002px;width:918px;height:54px"><span>Please upload your resume*
  <svg width="22" height="16" viewBox="0 0 22 16" style="vertical-align:-3px;margin-left:6px"><path d="M5 15h12a4.5 4.5 0 0 0 .6-9A6 6 0 0 0 6 5.5 4.8 4.8 0 0 0 5 15z" fill="#faa641"/><path d="M11 13V7m-3 3 3-3 3 3" stroke="#fffffe" stroke-width="1.6" fill="none"/></svg></span></div>
<p class="hint" style="top:3069px">Allowed file types: <b>PDF, DOC, DOCX</b></p>
<p class="hint" style="top:3091px">Max. file size: <b>10MB</b></p>

<div class="field" style="left:140px;top:3132px;width:918px;height:122px"><span>Would you like to share any public social media accounts?</span></div>
<p class="hint" style="top:3269px">This step is optional. If you are comfortable, you can include your professional social media accounts like a networking profile.</p>

<div class="abs apply-btn">Apply</div>

<!-- contact call to action -->
<div class="abs cta-photo" role="img" aria-label="Photo of a technician giving a lip treatment to a client"></div>
<footer class="footer"></footer>
<svg class="abs" style="left:0;top:3780px" width="1200" height="160" viewBox="0 0 1200 160" aria-hidden="true">
  <path d="M0 40 C250 80 420 150 640 100 C850 50 1000 40 1200 110 L1200 160 L0 160Z" fill="#faa641"/>
  <path d="M0 30 C250 60 420 120 640 80 C850 40 1000 20 1200 80 L1200 160 L0 160Z" fill="#000"/>
</svg>
<div class="abs cta-circle">
  <p>IF YOU HAVE ANY<br>QUESTIONS, PLEASE<br>CONTACT US.</p>
  <div class="cta-btn">BOOK ONLINE</div>
</div>

<div class="brand" style="left:140px;top:4044px;font-size:19px;color:#fffffe">
  <span class="brand-dot" style="width:28px;height:28px"></span>WILLOW GLOW &amp; LASER
</div>
<svg class="abs" style="left:140px;top:4110px" width="32" height="32" viewBox="0 0 32 32" aria-hidden="true"><circle cx="16" cy="16" r="14" fill="none" stroke="#faa641" stroke-width="3"/><path d="M16 8v8l5 3" stroke="#faa641" stroke-width="3" fill="none"/></svg>
<p class="foot-t" style="left:185px;top:4106px">WORKING HOURS<br>MON - FRI : 9AM – 6PM<br>SAT : Appointment Only</p>
<svg class="abs" style="left:140px;top:4188px" width="32" height="24" viewBox="0 0 32 24" aria-hidden="true"><rect x="1" y="1" width="30" height="22" rx="2" fill="#faa641"/><path d="M2 3l14 10 14-10" stroke="#000" stroke-width="2" fill="none"/></svg>
<p class="foot-t" style="left:185px;top:4186px">EMAIL<br>hello@willowglowlaser.example</p>

<h3 class="foot-h" style="left:505px;top:4043px">QUICK LINKS</h3>
<ul class="quick">
  <li class="on">HOME</li><li>SERVICES</li><li>PRICING</li><li>ABOUT</li><li>BLOG</li><li>CONTACT</li>
</ul>

<h3 class="foot-h" style="left:777px;top:4043px">NEWSLETTER SIGNUP</h3>
<p class="foot-t" style="left:777px;top:4078px;width:290px">Subscribe To Our Newsletter To Get The Latest Update To Your Inbox</p>
<div class="abs news-input">Enter your email</div>
<div class="abs news-btn">SUBSCRIBE</div>

<div class="abs" style="left:140px;top:4283px;width:918px;height:1px;background:#333"></div>
<p class="foot-t" style="left:140px;top:4294px;line-height:21px">© 2024 Willow Glow &amp; Laser. All Rights Reserved. – Privacy Policy • Terms &amp; Conditions<br>Medical Director: Dr. Morgan Ellery, NMD License #00-4821 Contact: md@willowglowlaser.example</p>
<span class="social" style="left:989px"></span>
<span class="social" style="left:1028px"></span>

</body>
</html>
```